Modern UI App Design

We need to have a proper design for a web app that we currently mocked in Powerpoint (will be provided). This PPT contains about 15 slides. The final app will have about 5-6 screens but with context sensitive elements. we would prefer a workflow based UI, i.e. screens should not be clogged but the interface should behave like a wizard or an TK Modern UI app.

- Design should be flat and should be Modern UI / Metro Style (using this as a design language and tiles / colors)
- The final result has to be much more designed, modern and homogeneous than now.
- We would also need a clickable HTML(5) prototype of the design, please let us know how this can be achieved
- Internet connection does not matter for the project, so has to work just within a browser but does not need to connect to a server (could even be local files)
- This does not need to be a fully functional HTML 5 page, after all it is a prototype / screen design, so it would be more like mouse over / clicking / moving to next screen
- If you cannot deliver HTML5 then please suggest providing something that we can edit easily ourselves (e.g. a Powerpoint again)
- LOOP is the name of our product

Target Market(s)

Financial institutions

Industry/Entity Type

Internet

Requirements
Must have
• Modern UI / Metro design

```html
<!DOCTYPE html>
<html lang="en">
<head>
<meta charset="utf-8">
<title>LOOP Data Management – Golder Price</title>
<link rel="stylesheet" href="https://fonts.googleapis.com/css2?family=Open+Sans:wght@400;600;700&display=swap">
<style>
  :root {
    --blue: #2a98ef;
    --blue-dark: #1f88dc;
    --tile: #ffffff;
    --label-bg: #e6e6e6;
    --text: #3d3d3d;
    --muted: #a9adb2;
    --bg-a: #3a3d42;
    --bg-b: #1d1f22;
    --zip: #1e9fd1;
    --pdf: #ef5350;
    --xls: #1fae8f;
    --share: #2a98ef;
    --strip: #e8e8e8;
  }
  * { box-sizing: border-box; margin: 0; padding: 0; }
  html, body { width: 1200px; height: 900px; overflow: hidden; }
  body {
    position: relative;
    font-family: "Open Sans", sans-serif;
    color: var(--text);
    background: radial-gradient(ellipse at 70% 40%, var(--bg-a) 0%, #2a2c30 45%, var(--bg-b) 100%);
  }
  .backdrop { position: absolute; inset: 0; }

  /* top bar */
  .brand {
    position: absolute; left: 12px; top: 12px; width: 208px; height: 80px;
    background: var(--blue); color: #fff; padding: 12px 14px;
  }
  .brand-name { font-size: 38px; font-weight: 700; line-height: 40px; letter-spacing: 2px; }
  .brand-sub { font-size: 15px; text-align: right; margin-top: 2px; }

  .context-tile {
    position: absolute; top: 12px; height: 80px; background: var(--tile);
    display: flex; align-items: center; padding-left: 13px;
  }
  .context-icon {
    width: 55px; height: 55px; background: var(--blue); border-radius: 3px;
    display: flex; align-items: center; justify-content: center; flex: none;
  }
  .context-text { margin-left: 17px; }
  .context-title { font-size: 16.5px; font-weight: 600; color: var(--muted); letter-spacing: .3px; line-height: 20px; }
  .context-sub { font-size: 10px; color: #b9bcc0; letter-spacing: .4px; margin-top: 2px; }
  .tile-security { left: 232px; width: 315px; }
  .tile-portfolio { left: 559px; width: 282px; }
  .tile-export { left: 854px; width: 281px; }
  .info-button {
    position: absolute; left: 1147px; top: 12px; width: 40px; height: 39px; background: var(--tile);
    display: flex; align-items: center; justify-content: center;
  }

  /* side navigation */
  .nav-tile {
    position: absolute; left: 11px; width: 137px; height: 137px; background: var(--tile);
    color: var(--blue); font-size: 16px; text-align: center;
    display: flex; flex-direction: column; align-items: center; justify-content: flex-end; padding-bottom: 12px;
  }
  .nav-tile svg { margin-bottom: 16px; }
  .nav-tile.active { background: var(--blue); color: #fff; }

  /* content */
  .toolbar {
    position: absolute; left: 199px; top: 123px; width: 642px; height: 53px; background: var(--blue);
  }
  .export-strip {
    position: absolute; right: 0; top: 0; height: 53px; width: 192px; background: var(--strip);
    display: flex; align-items: center; gap: 5px; padding-left: 5px;
  }
  .export-btn {
    width: 42px; height: 42px; color: #fff; font-weight: 700; font-size: 13px;
    display: flex; align-items: flex-end; justify-content: center; padding-bottom: 6px; position: relative;
  }
  .export-btn::before {
    content: ""; position: absolute; right: 0; top: 0; border-style: solid; border-width: 0 11px 11px 0;
    border-color: transparent var(--strip) rgba(0,0,0,.25) transparent;
  }
  .btn-zip { background: var(--zip); }
  .btn-pdf { background: var(--pdf); }
  .btn-xls { background: var(--xls); }
  .btn-share { background: var(--share); align-items: center; padding: 0; }
  .btn-share::before { display: none; }

  .panel { position: absolute; left: 199px; width: 642px; background: var(--tile); }
  .panel-price { top: 190px; height: 398px; }
  .panel-policy { top: 600px; height: 123px; }
  .panel-icon {
    position: absolute; left: 6px; top: 6px; width: 113px; height: 112px; background: var(--blue);
    display: flex; align-items: center; justify-content: center;
  }
  .panel-policy .panel-icon { height: 111px; }
  .panel-action {
    position: absolute; top: 341px; width: 54px; height: 52px; background: var(--blue);
    display: flex; align-items: center; justify-content: center;
  }
  .action-user { left: 6px; }
  .action-search { left: 65px; }

  .field-list { position: absolute; left: 124px; top: 6px; right: 4px; list-style: none; }
  .field {
    display: flex; height: 43px; margin-bottom: 6.2px; font-size: 14px;
  }
  .field-label {
    width: 250px; background: var(--label-bg); padding-left: 14px; display: flex; align-items: center; font-weight: 600; color: #4a4a4a;
  }
  .field-value {
    flex: 1; margin-left: 2px; border: 1px solid #e6e6e6; display: flex; align-items: center; justify-content: flex-end; padding-right: 14px;
  }
</style>
</head>
<body>
  <div class="backdrop" role="img" aria-label="Dark charcoal faceted polygon background"></div>

  <header>
    <div class="brand">
      <div class="brand-name">LOOP</div>
      <div class="brand-sub">Data Management</div>
    </div>

    <div class="context-tile tile-security">
      <div class="context-icon">
        <svg width="26" height="26" viewBox="0 0 26 26" fill="#fff"><rect x="4" y="13" width="4" height="10"/><rect x="11" y="5" width="4" height="18"/><rect x="18" y="10" width="4" height="13"/></svg>
      </div>
      <div class="context-text">
        <div class="context-title">NORVEX CORP 1.25% SR NTS<br>02/06/17</div>
        <div class="context-sub">NVX17A ATLX CORPORATE BOND</div>
      </div>
    </div>

    <div class="context-tile tile-portfolio">
      <div class="context-icon">
        <svg width="30" height="26" viewBox="0 0 30 26" fill="#fff"><path d="M10 4V2h10v2h7v19H3V4zm2 0h6V3.5h-6z"/><rect x="7" y="4" width="2" height="19" fill="#2a98ef"/><rect x="21" y="4" width="2" height="19" fill="#2a98ef"/></svg>
      </div>
      <div class="context-text">
        <div class="context-title">FIXED HOME</div>
        <div class="context-sub">PORFOLIO</div>
      </div>
    </div>

    <div class="context-tile tile-export">
      <div class="context-icon">
        <svg width="30" height="30" viewBox="0 0 30 30"><circle cx="15" cy="15" r="12" fill="none" stroke="#fff" stroke-width="3"/><path d="M15 8v8h6" fill="none" stroke="#fff" stroke-width="3"/></svg>
      </div>
      <div class="context-text">
        <div class="context-title">EXPORT</div>
        <div class="context-sub">12/03/2014 18:02</div>
      </div>
    </div>

    <div class="info-button">
      <svg width="30" height="30" viewBox="0 0 30 30"><circle cx="15" cy="15" r="14" fill="#2a98ef"/><circle cx="16" cy="8.5" r="2.2" fill="#fff"/><path d="M12 13h5l-2 9h3v2h-6l2-9h-2z" fill="#fff"/></svg>
    </div>
  </header>

  <nav>
    <div class="nav-tile active" style="top:123px">
      <svg width="66" height="62" viewBox="0 0 66 62"><path d="M36 4h22a4 4 0 0 1 4 4v22L30 62 4 36z" fill="#fff"/><circle cx="50" cy="16" r="5" fill="#2a98ef"/></svg>
      Golder Price
    </div>
    <div class="nav-tile" style="top:274px">
      <svg width="46" height="66" viewBox="0 0 46 66" fill="none" stroke="#2a98ef" stroke-width="4"><rect x="3" y="8" width="40" height="55" rx="3"/><rect x="15" y="2" width="16" height="10" rx="2" fill="#2a98ef"/><path d="M12 26h22M12 35h22M12 44h22M12 53h22"/></svg>
      Requests
    </div>
    <div class="nav-tile" style="top:425px">
      <svg width="66" height="62" viewBox="0 0 66 62"><path d="M36 4h22a4 4 0 0 1 4 4v22L30 62 4 36z" fill="#2a98ef"/><circle cx="50" cy="16" r="5" fill="#fff"/></svg>
      Silver Copies
    </div>
    <div class="nav-tile" style="top:578px">
      <svg width="46" height="66" viewBox="0 0 46 66" fill="none" stroke="#2a98ef" stroke-width="4"><rect x="3" y="8" width="40" height="55" rx="3"/><rect x="15" y="2" width="16" height="10" rx="2" fill="#2a98ef"/><path d="M12 36l8 8 14-15"/></svg>
      Plausibility
    </div>
    <div class="nav-tile" style="top:731px">
      <svg width="40" height="70" viewBox="0 0 40 70" fill="#2a98ef"><rect x="6" y="2" width="28" height="32" rx="3"/><rect x="17" y="34" width="6" height="8"/><path d="M20 40l5 9 10 1-7 7 2 10-10-5-10 5 2-10-7-7 10-1z"/></svg>
      Policy
    </div>
  </nav>

  <main>
    <div class="toolbar">
      <div class="export-strip">
        <div class="export-btn btn-zip">ZIP</div>
        <div class="export-btn btn-pdf">PDF</div>
        <div class="export-btn btn-xls">XLS</div>
        <div class="export-btn btn-share">
          <svg width="24" height="24" viewBox="0 0 24 24" fill="#fff"><circle cx="18" cy="5" r="3.2"/><circle cx="6" cy="12" r="3.2"/><circle cx="18" cy="19" r="3.2"/><path d="M6 12L18 5M6 12l12 7" stroke="#fff" stroke-width="2"/></svg>
        </div>
      </div>
    </div>

    <section class="panel panel-price">
      <div class="panel-icon">
        <svg width="90" height="82" viewBox="0 0 90 82" fill="#fff">
          <g><rect x="2" y="30" width="40" height="9" rx="4.5"/><rect x="2" y="41" width="40" height="9" rx="4.5"/><rect x="2" y="52" width="40" height="9" rx="4.5"/><rect x="2" y="63" width="40" height="9" rx="4.5"/></g>
          <g><rect x="36" y="4" width="40" height="9" rx="4.5"/><rect x="36" y="15" width="40" height="9" rx="4.5"/><rect x="36" y="26" width="40" height="9" rx="4.5"/></g>
          <g><rect x="46" y="38" width="40" height="9" rx="4.5"/><rect x="46" y="49" width="40" height="9" rx="4.5"/><rect x="46" y="60" width="40" height="9" rx="4.5"/><rect x="46" y="71" width="40" height="9" rx="4.5"/></g>
        </svg>
      </div>
      <div class="panel-action action-user">
        <svg width="34" height="34" viewBox="0 0 34 34" fill="#fff"><rect x="10" y="2" width="14" height="16" rx="6"/><path d="M2 32c0-8 6-12 15-12s15 4 15 12z"/></svg>
      </div>
      <div class="panel-action action-search">
        <svg width="34" height="34" viewBox="0 0 34 34" fill="none" stroke="#fff" stroke-width="3"><circle cx="14" cy="14" r="10"/><path d="M21 21l10 10" stroke-width="4"/></svg>
      </div>
      <ul class="field-list">
        <li class="field"><span class="field-label">Price Value</span><span class="field-value">187,24</span></li>
        <li class="field"><span class="field-label">Currency</span><span class="field-value">USD</span></li>
        <li class="field"><span class="field-label">Price Date</span><span class="field-value">10.03.2014</span></li>
        <li class="field"><span class="field-label">Quotation Type</span><span class="field-value">Official Close</span></li>
        <li class="field"><span class="field-label">Market</span><span class="field-value">ATLX</span></li>
        <li class="field"><span class="field-label">Data Source</span><span class="field-value">Quotient</span></li>
        <li class="field"><span class="field-label">Price Unit</span><span class="field-value">Piece</span></li>
        <li class="field"><span class="field-label">IFRS 13</span><span class="field-value">Level 1</span></li>
      </ul>
    </section>

    <section class="panel panel-policy">
      <div class="panel-icon">
        <svg width="40" height="70" viewBox="0 0 40 70" fill="#fff"><rect x="6" y="2" width="28" height="32" rx="3"/><rect x="17" y="34" width="6" height="8"/><path d="M20 40l5 9 10 1-7 7 2 10-10-5-10 5 2-10-7-7 10-1z"/></svg>
      </div>
      <ul class="field-list">
        <li class="field"><span class="field-label">Pricing Policy</span><span class="field-value">Standard EOD</span></li>
        <li class="field"><span class="field-label">Pricing Method</span><span class="field-value">US Bonds</span></li>
      </ul>
    </section>
  </main>
</body>
</html>
```